Flyer-Design für gehobenen Fahrzeugpflege
Zielgruppe
Wir sind in der gehobenen Fahrzeugpflege tätig und wollen den anspruchsvollen Kunden davon überzeugen Ihre Fahrzeuge regelmässig von uns aufwendig pflegen zu lassen.
Zielgruppe sind alle Fahrzeughalter ab dem Mittelstand. Aber auch Fahrzeuge die schwer verunreinigt sind, von Erbrochenem hin bis stark verrauchte Innenräume.
Aufgabenstellung
Format wäre DIN A4 für die Gestaltung eines Flyers. Texte findet man auch unter www.kesselmoor.de oder www.tg-wurzmoor.de
Mir kommt es auf den richtigen Slogan an, der den Kunden mit Anspruch direkt anspricht. Auch werden keine Preise genannt.
Uns geht es mehr darum dem Kunden darzustellen wie aufwendig und zeitintensiv ein Auto gereinigt werden kann im High end Bereich.

```html
<!DOCTYPE html>
<html lang="de">
<head>
<meta charset="utf-8">
<title>Kesselmoor – Flyer Fahrzeugpflege</title>
<link href="https://fonts.googleapis.com/css2?family=Raleway:wght@300;400;500;600;700;800&family=Montserrat:wght@400;500;700&display=swap" rel="stylesheet">
<style>
  :root{
    --stage:#dcdcdc;
    --gold:#d4b273;
    --gold-deep:#c9a35e;
    --ink:#121212;
    --dark-top:#232323;
    --dark-bottom:#0c0c0c;
    --paper:#ffffff;
    --text:#333333;
    --muted:#a8a8a8;
    --panel-grey:#262626;
  }
  *{box-sizing:border-box;margin:0;padding:0}
  html,body{width:1200px;height:3610px;overflow:hidden}
  body{background:var(--stage);position:relative;font-family:"Raleway",sans-serif;color:var(--text)}

  .panel{position:absolute;overflow:hidden;box-shadow:0 3px 10px rgba(0,0,0,.25)}
  .dark{background:linear-gradient(180deg,var(--dark-top),var(--dark-bottom))}
  .gold-band{position:absolute;left:0;right:0;bottom:0;height:14px;background:var(--gold)}

  .view-label{position:absolute;font-family:"Montserrat",sans-serif;color:var(--ink)}
  .view-label strong{display:block;font-size:31px;font-weight:700;line-height:1.1}
  .view-label span{display:block;font-size:23px;font-weight:400;line-height:1.3}
  .view-label.right{text-align:right}

  /* brand lockup */
  .lockup{position:absolute;left:0;right:0;text-align:center}
  .brand-word{font-family:"Raleway",sans-serif;font-weight:800;font-size:66px;color:#e6e6e6;line-height:1;letter-spacing:1px}
  .tagline{margin-top:18px;font-family:"Montserrat",sans-serif;font-size:16px;color:var(--gold);letter-spacing:2.2px;font-weight:500}
  .tagline b{font-weight:700}

  /* claim section */
  .claim{position:absolute;left:0;top:0;width:714px;height:352px;background:var(--paper)}
  .claim .kicker{position:absolute;left:35px;top:28px;font-size:34px;font-weight:800;color:var(--gold);letter-spacing:.5px}
  .claim .title{position:absolute;left:270px;top:28px;font-size:33px;font-weight:300;color:var(--gold);letter-spacing:.3px}
  .claim .copy{position:absolute;left:272px;top:80px;width:412px;font-size:11.4px;line-height:16.8px;color:#444}
  .claim .copy p{margin-bottom:17px}
  .claim .copy b{font-weight:700;color:#111}
  .claim .brand-name{position:absolute;left:32px;top:252px;font-size:40px;font-weight:800;color:var(--ink)}

  .badge{position:absolute;width:154px;height:154px;border-radius:50%;background:var(--gold);color:#fff;display:flex;flex-direction:column;align-items:center;justify-content:center;text-align:center;line-height:1;font-size:27px;letter-spacing:.5px}
  .badge b{font-weight:800}
  .badge span{font-weight:500}

  .car-photo{position:absolute;background:radial-gradient(ellipse at 55% 55%,#f4f4f4 0%,#dedede 45%,#9d9d9d 75%,rgba(60,60,60,0) 100%);border-radius:40% 45% 30% 30%}
  .slogan{position:absolute;right:51px;text-align:right;font-size:17px;line-height:24px;font-weight:400;color:var(--gold);letter-spacing:.6px}

  /* services */
  .services-head{position:absolute;left:35px;top:387px;font-size:35px;font-weight:800;color:var(--gold)}
  .services-intro{position:absolute;left:35px;top:436px;width:420px;font-size:12px;line-height:17px;font-weight:600;color:var(--gold)}
  .svc{position:absolute;color:#fff}
  .svc h3{font-size:17px;font-weight:800;color:var(--gold);margin-bottom:4px;letter-spacing:.2px}
  .svc ul{list-style:none}
  .svc li{font-size:10.2px;font-weight:700;line-height:13px;padding-left:9px;position:relative;margin-bottom:2px}
  .svc li::before{content:"•";position:absolute;left:0;color:var(--gold)}
  .svc li small{display:block;font-size:8.6px;font-weight:400;color:var(--muted);line-height:11px}
  .svc .note{font-size:10.2px;font-weight:700;margin:3px 0 4px}
  .svc .lead{font-size:8.6px;color:var(--muted);padding-left:9px;margin-bottom:4px}
  .svc .fn{font-size:7.2px;color:var(--muted);line-height:10px;margin-top:6px}
  .menus{position:absolute;left:418px;top:805px;width:279px;height:170px;border:1px solid var(--gold);padding:10px 14px}
  .menus h3{font-size:17px;font-weight:800;color:var(--gold);margin-bottom:6px}
  .menus p{font-size:8.6px;line-height:11.4px;color:var(--muted);margin-bottom:6px}
  .menus p b{color:var(--gold);font-weight:700}

  /* contact */
  .contact-head{position:absolute;left:52px;top:351px;font-size:21px;font-weight:800;color:#fff;letter-spacing:.2px}
  .contact-card{position:absolute;left:49px;top:384px;width:613px;height:256px;display:flex}
  .contact-info{width:239px;background:var(--panel-grey);position:relative;color:#fff}
  .contact-info .company{position:absolute;left:56px;top:24px;font-size:15px;font-weight:700}
  .c-line{position:absolute;left:26px;display:flex;align-items:flex-start;gap:14px;font-size:15px;line-height:19px;font-weight:500}
  .c-line svg{flex:none;margin-top:2px}
  .hours{position:absolute;left:0;right:0;bottom:0;height:73px;background:var(--gold);color:var(--ink);padding:11px 14px}
  .hours h4{font-size:17px;font-weight:800;padding-bottom:5px;border-bottom:1px solid rgba(0,0,0,.55);letter-spacing:.3px}
  .hours p{font-size:17px;font-weight:500;margin-top:6px}
  .map{flex:1;background:linear-gradient(135deg,#ececec,#dcdcdc 55%,#e6e6e6)}
</style>
</head>
<body>

<!-- FRONT -->
<section class="panel dark" style="left:98px;top:104px;width:714px;height:340px">
  <div class="lockup" style="top:110px">
    <div class="brand-word">Kesselmoor</div>
    <div class="tagline">FAHRZEUGPFLEGE <b>IM DETAIL</b></div>
  </div>
  <div class="gold-band"></div>
</section>
<div class="view-label" style="left:844px;top:232px"><strong>FRONT (quer)</strong><span>Wird nach oben geklappt</span></div>

<!-- INNEN I -->
<section class="panel" style="left:419px;top:526px;width:714px;height:680px;background:var(--paper)">
  <div class="claim">
    <div class="kicker">ANSPRUCH</div>
    <div class="title">WARUM ZU KESSELMOOR?</div>
    <div class="copy">
      <p>Eine Fahrzeugreinigung erhalten Sie überall,<br><b>Fahrzeugpflege im Detail nur bei uns!</b></p>
      <p>Allerhöchste Ansprüche in der Ausführung und im Endergebnis sind für uns ganz entscheidende Unterschiede in der Qualität und Ihr persönlicher Vorteil. Unsere langjährige Erfahrung in der professionellen Fahrzeugpflege und die Liebe zum Detail veranlassen uns das beste Ergebnis für Ihr Fahrzeug zu erzielen. In der Praxis zeigt sich immer wieder, dass selbst Neuwagen im Luxussegment bei der Auslieferung vom Hersteller ungenügend aufbereitet sind.</p>
      <p><b>Geben Sie Ihrem Fahrzeug das Prädikat «Besser als Neu».<br>Dafür steht der Name Kesselmoor!</b></p>
    </div>
    <div class="brand-name">Kesselmoor</div>
  </div>
  <div class="dark" style="position:absolute;left:0;top:513px;width:714px;height:167px"></div>
  <div class="car-photo" role="img" aria-label="Foto eines weißen Cabrios in Frontansicht" style="left:27px;top:388px;width:453px;height:219px"></div>
  <div class="badge" style="left:526px;top:318px"><b>BESSER</b><span>ALS NEU</span></div>
  <div class="slogan" style="top:580px">AUFWENDIG.<br>IN PERFEKTION.<br>MASSGESCHNEIDERT.</div>
</section>
<div class="view-label right" style="right:814px;top:952px"><strong>INNEN I</strong><span>Wird nach unten geklappt</span></div>

<!-- INNEN II -->
<section class="panel dark" style="left:90px;top:1333px;width:714px;height:1008px">
  <div class="claim" style="height:357px">
    <div class="kicker">ANSPRUCH</div>
    <div class="title">WARUM ZU KESSELMOOR?</div>
    <div class="copy">
      <p>Eine Fahrzeugreinigung erhalten Sie überall,<br><b>Fahrzeugpflege im Detail nur bei uns!</b></p>
      <p>Allerhöchste Ansprüche in der Ausführung und im Endergebnis sind für uns ganz entscheidende Unterschiede in der Qualität und Ihr persönlicher Vorteil. Unsere langjährige Erfahrung in der professionellen Fahrzeugpflege und die Liebe zum Detail veranlassen uns das beste Ergebnis für Ihr Fahrzeug zu erzielen. In der Praxis zeigt sich immer wieder, dass selbst Neuwagen im Luxussegment bei der Auslieferung vom Hersteller ungenügend aufbereitet sind.</p>
      <p><b>Geben Sie Ihrem Fahrzeug das Prädikat «Besser als Neu».<br>Dafür steht der Name Kesselmoor!</b></p>
    </div>
    <div class="brand-name">Kesselmoor</div>
  </div>
  <div class="badge" style="left:526px;top:320px"><b>BESSER</b><span>ALS NEU</span></div>

  <h2 class="services-head">LEISTUNGEN</h2>
  <p class="services-intro">Unser Arbeitsaufwand ergibt sich unabhängig vom Typ und der Größe eines Fahrzeuges. Preise ergeben sich erst nach Besichtigung und eines persönlichen Gesprächs vor Ort.</p>

  <div class="svc" style="left:35px;top:526px;width:195px">
    <h3>LACKREIN</h3>
    <ul><li>Manuelle Oberwäsche<small>Einweichen, Shampoonieren, Abledern</small></li></ul>
    <div class="note">Entfernung von:</div>
    <ul>
      <li>Insekten-Rückständen<small>Einweichen, Shampoonieren, Insektenrückstände entfernen</small></li>
      <li>Vogelkot<small>Einweichen, Shampoonieren, Vogelkot entfernen</small></li>
      <li>Baumharz-Rückständen<small>Analysieren, Baumharz entfernen, Waschen</small></li>
      <li>Flugrost-Belägen<small>Analysieren, Flugrost abkneten, Waschen</small></li>
      <li>Teer-Rückständen<small>Analysieren, Teer entfernen, Waschen</small></li>
      <li>Aufklebern</li>
    </ul>
  </div>

  <div class="svc" style="left:244px;top:526px;width:205px">
    <h3>FELGENREIN</h3>
    <div class="lead">Reinigen, Schleifen, Polieren, Versiegeln</div>
    <ul>
      <li>Chrom Felge*<small>Reinigen, Schleifen, Polieren, Versiegeln</small></li>
      <li>Aluminium Felge*<small>Reinigen, Polieren, Versiegeln</small></li>
      <li>Kohlefaser Felge<br>(Carbon Felge)*<small>Reinigen, Polieren, Versiegeln**</small></li>
      <li>Drahtspeichen Felge*<small>Reinigen, Polieren, Versiegeln</small></li>
      <li>Holzspeichen Felge*<small>Reinigen, Polieren, Versiegeln</small></li>
      <li>Dreiteilige Felge*<small>Reinigen, Polieren, Versiegeln</small></li>
    </ul>
    <div class="fn">* auf Wunsch mit Demontage<br>** auf Wunsch mit 1K-Nano Versiegelung</div>
  </div>

  <div class="svc" style="left:469px;top:526px;width:230px">
    <h3>CABRIO VERDECKREIN</h3>
    <ul>
      <li>Cabrio Verdeckreinigung<small>Reinigung und Beseitigung von Belägen</small></li>
      <li>Schimmelbeseitigung</li>
      <li>Farbkorrektur</li>
      <li>Vinylscheiben Politur</li>
      <li>Imprägnierung</li>
    </ul>
    <h3 style="margin-top:20px">LACKFEIN</h3>
    <ul>
      <li>Schleifpolitur<small>Zur Vorbereitung der Lackoberfläche</small></li>
      <li>Feinschleifpolitur<small>Feinbearbeitung der Lackoberfläche</small></li>
      <li>Antihologramm Politur</li>
      <li>Wachspolitur</li>
      <li>1K- Nano Versiegelung</li>
    </ul>
  </div>

  <div class="svc" style="left:35px;top:829px;width:195px">
    <h3>DETAILREIN</h3>
    <ul>
      <li>Chrom Komponenten<small>Schleifen, Polieren, Versiegeln</small></li>
      <li>Aluminium Komponenten<small>Schleifen, Polieren, Versiegeln</small></li>
      <li>Kunststoff Komponenten<small>Reinigen, Pflegen, Farblich auffrischen</small></li>
      <li>Gummi Komponenten<small>Reinigen, Pflegen, Farblich auffrischen</small></li>
    </ul>
  </div>

  <div class="svc" style="left:244px;top:816px;width:168px">
    <h3>PANNENFEIN</h3>
    <ul>
      <li>Dellen Entfernung</li>
      <li>Beseitigung von Fassadenfarbe und Graffiti</li>
      <li>Beseitigung von Betonresten und Säurerückständen</li>
      <li>Lackierarbeiten / Pulvern</li>
      <li>Felgen Reparatur</li>
      <li>Beschaffung von Ersatzteilen</li>
      <li>Montage von Ersatzteilen</li>
    </ul>
  </div>

  <div class="menus">
    <h3>MENÜS</h3>
    <p><b>Lackfein I</b> Waschen, reinigen und polieren der Holme und Lackoberflächen, Versiegelung mit Carnaubawachs</p>
    <p><b>Lackfein II</b> Waschen, schleifen und polieren der Holme und Lackoberflächen, im Anschluss Antihologramm-Versiegelung</p>
    <p><b>Felgenrein I</b> Von Hand shampooniert, Antihologramm-Versiegelung versehen. Die Reifen werden mit einem Conditioner gepflegt.</p>
    <p><b>Felgenrein II</b> (Demontage, von Hand shampooniert, Versiegelung mit Nano-Politur</p>
  </div>
  <div class="gold-band"></div>
</section>
<div class="view-label" style="left:844px;top:1776px"><strong>INNEN II</strong><span>ganz geöffnet</span></div>

<!-- AUSSEN -->
<section class="panel dark" style="left:419px;top:2504px;width:714px;height:1009px">
  <div style="position:absolute;left:0;top:0;width:714px;height:161px;background:var(--paper)"></div>
  <div class="car-photo" role="img" aria-label="Foto eines weißen Cabrios in Frontansicht" style="left:27px;top:34px;width:453px;height:224px"></div>
  <div class="badge" style="left:526px;top:-29px"><b>BESSER</b><span>ALS NEU</span></div>
  <div class="slogan" style="top:230px">AUFWENDIG.<br>IN PERFEKTION.<br>MASSGESCHNEIDERT.</div>

  <h2 class="contact-head">IHRE ADRESSE FÜR DIE GEHOBENE FAHRZEUGPFLEGE.</h2>
  <div class="contact-card">
    <div class="contact-info">
      <div class="company">Kesselmoor UG</div>
      <div class="c-line" style="top:50px">
        <svg width="16" height="16" viewBox="0 0 16 16"><circle cx="8" cy="8" r="8" fill="var(--gold)"/><path d="M4 8.5 8 5l4 3.5V12H4z" fill="#262626"/></svg>
        <span>Lindenweg 14<br>30159 Hannover</span>
      </div>
      <div class="c-line" style="top:95px">
        <svg width="16" height="16" viewBox="0 0 16 16"><circle cx="8" cy="8" r="8" fill="var(--gold)"/><path d="M5 4.5c1-.6 1.6 1.5 1 2.2-.3.3 1.6 2.6 2.3 2.3.7-.6 2.8 0 2.2 1-.6 1-2.2 1.5-4-.3S4 5.1 5 4.5z" fill="#262626"/></svg>
        <span>+49 511 48 31 95 2</span>
      </div>
      <div class="c-line" style="top:115px">
        <svg width="16" height="16" viewBox="0 0 16 16"><circle cx="8" cy="8" r="8" fill="var(--gold)"/><rect x="4" y="5.5" width="8" height="5.5" fill="none" stroke="#262626" stroke-width="1"/><path d="M4 5.5 8 8.5l4-3" fill="none" stroke="#262626" stroke-width="1"/></svg>
        <span>info@kesselmoor.de</span>
      </div>
      <div class="c-line" style="top:143px">
        <svg width="16" height="16" viewBox="0 0 16 16"><circle cx="8" cy="8" r="8" fill="var(--gold)"/><circle cx="8" cy="8" r="4" fill="none" stroke="#262626" stroke-width="1"/><path d="M4 8h8M8 4c-2 2.5-2 5.5 0 8M8 4c2 2.5 2 5.5 0 8" fill="none" stroke="#262626" stroke-width=".8"/></svg>
        <span>www.kesselmoor.de</span>
      </div>
      <div class="hours">
        <h4>ÖFFNUNGSZEITEN:</h4>
        <p>Mo – Fr 08:00 – 17:00 Uhr</p>
      </div>
    </div>
    <div class="map" role="img" aria-label="Stadtplanausschnitt mit Standortmarkierung"></div>
  </div>

  <div class="lockup" style="top:780px">
    <div class="brand-word">Kesselmoor</div>
    <div class="tagline">FAHRZEUGPFLEGE <b>IM DETAIL</b></div>
  </div>
  <div class="gold-band"></div>
</section>
<div class="view-label right" style="right:814px;top:2966px"><strong>AUSSEN</strong><span>ganz geöffnet</span></div>

</body>
</html>
```